movie poster Dustwarden

Create a movie poster for a thriller/suspense/horror movie called Dustwarden which is about a monastery of sinister monks who are hell bent on destroying the world when three friends come on a photography assignment and find they may never escape!

A Helena Markby Film

Owen Trask -- Nolan
Megan Dorsey -- Ruth
Harold Plimpton -- Felix
Dale Fenwick --- Brother Ottavio
Lachlan Markby -- Brother Lorenzo
Thomas Elgood ---Father Anselmo
Bernard Oakes -- Cardinal Vespoli
with Walter Kessing --- Gas Station Attendant

Helena Markby -- Writer, Director, Producer
Dennis Plimpton -- Director of Photography
Harold Plimpton -- Special Effects
Dennis Plimpton -- Editor
Curtis "Sparky" Villareal -- Sound

I just posted an update on the brief for the poster. Please include the credits on your movie poster. Thanks! I will be making a selection in the next few days.

Target Market(s)

This will be a PG and should attract a wide audience

Industry/Entity Type

Movie

Colors
eb1f27

Requirements
Must have
• Movie title, movie credits as provided
All material must be original --- no clip art or material taken from the internet
Nice to have
• tagline
Seeing is believing . . . until you believe what you don't see.

```html
<!DOCTYPE html>
<html lang="en">
<head>
<meta charset="utf-8">
<title>Dustwarden</title>
<link rel="stylesheet" href="https://fonts.googleapis.com/css2?family=Bebas+Neue&family=Creepster&family=Rubik+Dirt&display=swap">
<style>
  :root {
    --blood: #eb1f27;
    --blood-deep: #8a0d12;
    --shadow: #1a0a0b;
    --ink: #ffffff;
    --pale: #e9f7f6;
  }
  * { margin: 0; padding: 0; box-sizing: border-box; }
  html, body { width: 810px; height: 1200px; overflow: hidden; background: var(--shadow); }
  .poster {
    position: relative;
    width: 810px;
    height: 1200px;
    overflow: hidden;
    font-family: "Bebas Neue", "Arial Narrow", sans-serif;
    color: var(--ink);
  }
  .key-art {
    position: absolute; inset: 0;
    background:
      radial-gradient(ellipse 28% 22% at 78% 32%, rgba(255,240,240,0.75), transparent 70%),
      radial-gradient(ellipse 30% 55% at 52% 45%, #1c1112 0%, rgba(28,17,18,0.9) 55%, transparent 80%),
      radial-gradient(ellipse 90% 70% at 30% 40%, var(--blood) 0%, var(--blood-deep) 60%, var(--shadow) 100%);
  }
  .cast {
    position: absolute; left: 58px; top: 70px;
    list-style: none;
  }
  .cast li {
    font-size: 27px;
    letter-spacing: 0.5px;
    line-height: 1;
    height: 43.3px;
    text-shadow: 0 0 4px rgba(0,0,0,0.6);
  }
  .cast .as { font-size: 17px; margin: 0 8px; }
  .presenter {
    position: absolute; top: 660px; width: 100%;
    text-align: center;
    font-size: 32px; color: var(--pale);
    letter-spacing: 0.5px;
  }
  .presenter .small { font-size: 24px; }
  .title {
    position: absolute; top: 740px; width: 100%;
    text-align: center;
    font-family: "Creepster", "Impact", cursive;
    font-size: 132px; line-height: 1;
    color: var(--ink);
    letter-spacing: 2px;
    text-shadow: 0 4px 10px rgba(0,0,0,0.7);
  }
  .tagline {
    position: absolute; top: 928px; width: 100%;
    text-align: center;
    font-family: "Rubik Dirt", "Impact", sans-serif;
    font-size: 26px; letter-spacing: 0.5px;
    text-transform: uppercase;
  }
  .crew {
    position: absolute; left: 0; width: 100%;
    display: flex; justify-content: center; align-items: center;
    gap: 22px;
  }
  .crew-top { top: 1078px; }
  .crew-bottom { top: 1138px; }
  .credit { display: flex; align-items: center; gap: 7px; }
  .role {
    font-size: 11px; line-height: 1.0;
    text-transform: uppercase; text-align: right;
  }
  .role.inline { font-size: 22px; }
  .name { font-size: 30px; line-height: 1; }
</style>
</head>
<body>
<div class="poster">
  <div class="key-art" role="img" aria-label="Hooded monk figure in dark robes standing against a blood-red splattered backdrop"></div>

  <ul class="cast">
    <li>Owen Trask<span class="as">AS</span>Nolan</li>
    <li>Megan Dorsey<span class="as">AS</span>Ruth</li>
    <li>Harold Plimpton<span class="as">AS</span>Felix</li>
    <li>Dale Fenwick<span class="as">AS</span>Brother Ottavio</li>
    <li>Lachlan Markby<span class="as">AS</span>Brother Lorenzo</li>
    <li>Thomas Elgood<span class="as">AS</span>Father Anselmo</li>
    <li>Bernard Oakes<span class="as">AS</span>Cardinal Vespoli</li>
    <li><span class="as" style="margin-left:0">WITH</span>Walter Kessing<span class="as">AS</span>Gas Station Attendant</li>
  </ul>

  <p class="presenter">A Helena Markby <span class="small">FILM</span></p>
  <h1 class="title">DUSTWARDEN</h1>
  <p class="tagline">Seeing is believing . . . until you believe what you don't see.</p>

  <div class="crew crew-top">
    <div class="credit"><span class="role">Writer<br>Director<br>Producer</span><span class="name">Helena Markby</span></div>
    <div class="credit"><span class="role">Director of<br>Photography</span><span class="name">Dennis Plimpton</span></div>
    <div class="credit"><span class="role">Special<br>Effects</span><span class="name">Harold Plimpton</span></div>
  </div>
  <div class="crew crew-bottom">
    <div class="credit"><span class="role inline">Editor</span><span class="name">Dennis Plimpton</span></div>
    <div class="credit"><span class="role inline">Sound</span><span class="name">Curtis "Sparky" Villareal</span></div>
  </div>
</div>
</body>
</html>
```